Radon Reduction & Mold Removal Website

I need you to set up a WordPress account for me and design a full width, professional-looking, mobile-responsive website for my business. We offer radon reduction and mold removal (two household environmental issues).
We have merged 2 companies and need a single website to promote both services (radon and mold). Here are the current websites from the 2 businesses that have merged:
RADON
http://klendor-airfix.com/
MOLD
http://brisketfungusclear.net/
Once complete, I will need the login to the WordPress account so I have access to the site to make changes, additions, and modifications.
Target Market(s)
Home Owners
Industry/Entity Type
Home And Garden
Look and feel
Each slider illustrates characteristics of the customer's brand and the style your logo design should communicate.

```html
<!DOCTYPE html>
<html lang="en">
<head>
<meta charset="utf-8">
<title>Klendor Environmental – Radon Reduction &amp; Mold Removal</title>
<link href="https://fonts.googleapis.com/css2?family=Roboto:wght@300;400;500;700&family=Roboto+Condensed:wght@300;400&family=Open+Sans:wght@400;600;700&display=swap" rel="stylesheet">
<style>
:root{
  --header-bg:#161616;
  --accent-yellow:#f3e61c;
  --brand-green:#169a16;
  --bar-green:#0c9a0c;
  --text-grey:#7a7a7a;
  --text-dark:#333;
  --footer-bg:#343434;
  --footer-text:#e6e6e6;
  --divider:#e2e2e2;
}
*{margin:0;padding:0;box-sizing:border-box}
html,body{width:1077px;height:1200px;overflow:hidden;background:#fff}
body{position:relative;font-family:'Roboto',Arial,sans-serif;color:var(--text-dark)}
.abs{position:absolute}

/* header */
.site-header{left:0;top:0;width:1077px;height:93px;background:var(--header-bg);border-top:1px solid #000}
.nav-link{font-family:'Roboto Condensed',Arial,sans-serif;font-weight:300;font-size:17px;color:#fff;top:62px;letter-spacing:-.2px;white-space:nowrap}
.nav-link.active{color:var(--accent-yellow)}
.brand{left:483px;top:7px;width:109px;height:77px;background:#000;display:flex;flex-direction:column;align-items:center;justify-content:center;gap:5px}
.brand-square{width:14px;height:14px;background:var(--accent-yellow)}
.brand-name{font-family:'Roboto',sans-serif;font-weight:700;font-size:19px;color:var(--accent-yellow);letter-spacing:1px}
.phone{left:780px;top:12px;display:flex;align-items:center;gap:7px;font-family:'Open Sans',sans-serif;font-weight:600;font-size:13px;color:var(--accent-yellow)}

/* hero */
.hero{left:0;top:93px;width:1077px;height:322px;background:linear-gradient(180deg,#a9c0d8 0%,#c8d4dc 30%,#c9ab86 55%,#7d6a52 80%,#53613a 100%)}
.hero-caption{left:0;top:356px;width:1077px;height:59px;background:rgba(40,40,40,.55);color:#fff;text-align:center;font-weight:500;font-size:15px;line-height:20px;padding-top:10px}
.hero-shadow{left:215px;top:415px;width:647px;height:10px;background:radial-gradient(ellipse at top,rgba(0,0,0,.12),transparent 70%)}

/* welcome */
.welcome-title{left:0;width:1077px;top:440px;text-align:center;font-size:19px;font-weight:400;color:#444}
.welcome-title strong{color:var(--brand-green);font-weight:500}
.welcome-text{left:0;width:1077px;top:468px;text-align:center;font-size:10.4px;line-height:16.3px;letter-spacing:-.2px;color:var(--text-grey);white-space:nowrap}
.more-link{left:0;width:1077px;top:553px;text-align:center;font-size:11px;font-weight:500;color:var(--brand-green)}

/* services */
.service{width:205px;text-align:center}
.service-title{font-size:15px;font-weight:300;color:var(--brand-green);height:24px}
.service-photo{margin:0 auto}
.service-text{font-family:Arial,sans-serif;font-size:9.2px;line-height:12px;color:#333;margin-top:10px}
.col-divider{width:1px;top:611px;height:191px;background:var(--divider)}
.section-shadow{left:215px;top:806px;width:647px;height:10px;background:radial-gradient(ellipse at top,rgba(0,0,0,.08),transparent 70%)}

/* clients */
.clients-title{left:227px;top:856px;font-size:21px;font-weight:300;color:#222}
.clients-title strong{color:var(--brand-green);font-weight:500}
.client-name{font-size:13px;font-weight:500;color:#333;display:flex;align-items:center;gap:5px;white-space:nowrap}
.client-dot{width:8px;height:8px;border-radius:50%;background:#333}
.v-divider{left:651px;top:839px;width:1px;height:160px;border-left:1px dotted #bbb}
.portrait{left:705px;top:840px;width:100px;height:100px;border-radius:50%;background:radial-gradient(circle at 50% 40%,#cfcfcf,#8d8d8d)}
.quote{left:651px;width:216px;top:947px;text-align:center;font-family:Arial,sans-serif;font-size:9.5px;line-height:13px;color:#333}
.quote-author{left:651px;width:216px;top:981px;text-align:center;font-size:10px;color:#888}
.quote-author strong{color:var(--brand-green);font-weight:400;font-size:11px}

/* footer */
.site-footer{left:0;top:1027px;width:1077px;height:153px;background:var(--footer-bg);font-family:'Open Sans',sans-serif}
.footer-heading{font-size:12.5px;font-weight:600;color:var(--accent-yellow)}
.footer-list{list-style:none;margin-top:8px}
.footer-list li{font-size:9px;color:var(--footer-text);height:19px;line-height:19px}
.footer-list.tight li{height:17.5px;line-height:17.5px}
.social li{display:flex;align-items:center;gap:10px;height:26px;font-size:9px;color:var(--footer-text)}
.social-square{width:15px;height:15px;background:#f2f2f2;border-radius:2px}
.bottom-bar{left:0;top:1180px;width:1077px;height:20px;background:var(--bar-green);font-family:'Open Sans',sans-serif;font-size:8.5px;font-weight:600;color:#fff}
.copyright{left:210px;top:4px}
.legal{left:695px;top:4px;white-space:nowrap}
.legal span{margin:0 6px}
</style>
</head>
<body>

<header class="abs site-header">
  <nav>
    <span class="abs nav-link active" style="left:181px">HOME</span>
    <span class="abs nav-link" style="left:253px">ABOUT US</span>
    <span class="abs nav-link" style="left:351px">OUR&nbsp; SERVICES</span>
    <span class="abs nav-link" style="left:606px">OUR PROIDUCT</span>
    <span class="abs nav-link" style="left:733px">GET A QOUTE</span>
  </nav>
  <div class="abs brand">
    <div class="brand-square"></div>
    <div class="brand-name">KLENDOR</div>
  </div>
  <div class="abs phone">
    <svg width="19" height="16" viewBox="0 0 19 16" aria-hidden="true">
      <path d="M1 6 Q9.5 -1 18 6 L15 8 L13 5 Q9.5 3.5 6 5 L4 8 Z" fill="#f3e61c"/>
      <rect x="4" y="8" width="11" height="7" rx="1.5" fill="#f3e61c"/>
      <circle cx="9.5" cy="11.5" r="2" fill="#161616"/>
    </svg>
    (888) 555-0142
  </div>
</header>

<section class="abs hero" role="img" aria-label="Photo of a large suburban brick and stucco family home under a blue sky"></section>
<div class="abs hero-caption">Klendor Environmental is America's #1 Company in solving the dangers of radon gas.<br>We employ more certified mitigators than any other radon mitigation company.</div>
<div class="abs hero-shadow"></div>

<h1 class="abs welcome-title">Welcome to <strong>KLENDOR</strong></h1>
<p class="abs welcome-text">High levels of radon have been found in every state across America. Radon Mitigation and radon testing have become more prevalent in<br>the past few years in residential, commercial and real-estate environments with the real-estate market showing the biggest growth due<br>to some state and local real-estate regulations mandating the testing and mitigation of radon in homes on the market.&nbsp; wide and locally<br>in your areas. We install more than 10,000 radon systems yearly and have been dealing with radon mitigation since 1988. Radon Mitiga-<br>tion and radon removal is what we do and we are dedicated to providing quality radon mitigation services.</p>
<div class="abs more-link">Our More Services....</div>

<article class="abs service" style="left:209px;top:594px">
  <h2 class="service-title">Residential Services</h2>
  <div class="service-photo" role="img" aria-label="Photo of a worker on a ladder beside a house with siding" style="width:181px;height:98px;margin-top:10px;background:linear-gradient(90deg,#8a8276,#b9b3a8 50%,#6f7455)"></div>
  <p class="service-text">Lorem ipsum dolor sit amet,&nbsp; consectetur adipisic-ing elit, sed do eiusmod tempor incididunt ut labore&nbsp; et dolore magna aliqua. Ut enim ad minim veniam, quis nostrud exercitation ullamco laboris nisi ut aliquip ex ea commodo consequat.</p>
</article>
<div class="abs col-divider" style="left:426px"></div>
<article class="abs service" style="left:434px;top:596px">
  <h2 class="service-title">Commercial Services</h2>
  <div class="service-photo" role="img" aria-label="Photo of a radon vent pipe fitting against an exterior wall" style="width:160px;height:99px;margin-top:6px;background:linear-gradient(90deg,#bba98f,#d7c6a3 50%,#7e6c52)"></div>
  <p class="service-text">Lorem ipsum dolor sit amet,&nbsp; consectetur adipisic-ing elit, sed do eiusmod tempor incididunt ut labore&nbsp; et dolore magna aliqua. Ut enim ad minim veniam, quis nostrud exercitation ullamco laboris nisi ut aliquip ex ea commodo consequat.</p>
</article>
<div class="abs col-divider" style="left:650px"></div>
<article class="abs service" style="left:659px;top:597px">
  <h2 class="service-title">Real Estate Services</h2>
  <div class="service-photo" role="img" aria-label="Photo of office staff working at computers" style="width:162px;height:100px;margin-top:2px;background:linear-gradient(90deg,#a9b7c8,#e2e5ea 50%,#7c8796)"></div>
  <p class="service-text">Lorem ipsum dolor sit amet,&nbsp; consectetur adipisic-ing elit, sed do eiusmod tempor incididunt ut labore&nbsp; et dolore magna aliqua. Ut enim ad minim veniam, quis nostrud exercitation ullamco laboris nisi ut aliquip ex ea commodo consequat.</p>
</article>
<div class="abs section-shadow"></div>

<h2 class="abs clients-title"><strong>Client</strong> we work with.</h2>
<div class="abs client-name" style="left:228px;top:919px">Halvern Goods</div>
<div class="abs client-name" style="left:369px;top:919px"><span class="client-dot"></span>Crispfield</div>
<div class="abs client-name" style="left:454px;top:919px"><span class="client-dot"></span>Norvale Drinks</div>
<div class="abs client-name" style="left:580px;top:919px">Barberly</div>
<div class="abs client-name" style="left:228px;top:973px">Wrenmoor</div>
<div class="abs client-name" style="left:369px;top:973px">Telvanta</div>
<div class="abs client-name" style="left:500px;top:973px">Lumette</div>
<div class="abs client-name" style="left:574px;top:973px">Pebblo</div>

<div class="abs v-divider"></div>
<div class="abs portrait" role="img" aria-label="Black and white portrait of the company director"></div>
<p class="abs quote">Ventorix is unique in its versatility.<br>I think it's the wave of the future.</p>
<p class="abs quote-author"><strong>Director Name</strong> - Protection Halvern Goods</p>

<footer class="abs site-footer">
  <div class="abs" style="left:226px;top:12px">
    <h3 class="footer-heading">Company</h3>
    <ul class="footer-list"><li>Home</li><li>About Us</li><li>Careers</li><li>Events</li><li>Press Room</li></ul>
  </div>
  <div class="abs" style="left:454px;top:12px">
    <h3 class="footer-heading">Services</h3>
    <ul class="footer-list tight"><li>Service 1</li><li>Service 1</li><li>Service 1</li><li>Service 1</li><li>Service 1</li><li>Service 1</li></ul>
  </div>
  <div class="abs" style="left:779px;top:10px">
    <h3 class="footer-heading">Follow us on</h3>
    <ul class="footer-list social" style="margin-left:6px;margin-top:4px">
      <li><span class="social-square"></span>Chirpline</li>
      <li><span class="social-square"></span>Proflink</li>
      <li><span class="social-square"></span>Facelane</li>
      <li><span class="social-square"></span>Searchwell</li>
    </ul>
  </div>
</footer>
<div class="abs bottom-bar">
  <span class="abs copyright">Copyrights © 2015 klendor. All rights reserved.</span>
  <span class="abs legal">Terms of Use<span>|</span>Privacy Policy<span>|</span>Contat US</span>
</div>

</body>
</html>
```